Vitoplume.com

I need a web design for a Online Wellness Center based in Chicago, IL and it's called "Vitoplume" We provide Health risk assessment to individuals and interventions. Our portal has a Health Activity tracker where our members record health activities and aerobic miles and biometric data. Our Online wellness center tracks the participant's progress toward health goals and awards points for completed activities.
I started working on this website but the designer was not able to designer a website which describes what we do. I need a fresh look on this project. I need a very attractive, responsive website which says what we do.
These are the things we do.
1. We provide Health Risk Assessments to individuals and Co-operations
2. We Provide Free health screenings to undeserved communities
3. Assist individuals access free or affordable medications
4. We ask providers/doctors to see (or do a complete physical) one individual free of charge once a year (those individuals who are no insured and don't have money to pay from their pocket)
5. Assist patient access lab work at low cost
Our goal is to provide services that will lower the cost of care for our members.

Here is the website: www.vitoplume.com still underdevelopment. PLEASE DO NOT COPY THIS STYLE OF WEBSITE. IT'S A BAD DESIGN AND THAT IS WHY I'M RE-DESIGNING THE SITE

Target Market(s)

Health individuals between the age of 21 to 65 Plus years old. Insured and uninsured

Industry/Entity Type

Health And Wellness

Coding

Coded - Design and coding required

Number of Pages Required

5+ page

Colors
0292cd

Requirements
Must have
• I'm still working on this websiteHere is the menu: Home, About us, Services, Health Screening, Providers, Contacts
• Please see. www.vitoplume.com
Nice to have
• Event calender
• Upcoming Event
• Medication
• Lab assist
• Providers/Free Clinics

```html
<!DOCTYPE html>
<html lang="en">
<head>
<meta charset="utf-8">
<title>Vitoplume – Online Wellness Center</title>
<link href="https://fonts.googleapis.com/css2?family=Open+Sans:wght@400;600;700&display=swap" rel="stylesheet">
<style>
:root{
  --blue:#0292cd;
  --blue-dark:#0277ab;
  --ink:#333a40;
  --muted:#777f86;
  --line:#e2e6ea;
  --footer:#2b2e31;
  --footer-text:#a9aeb2;
  --white:#ffffff;
}
*{box-sizing:border-box;margin:0;padding:0}
html,body{width:1200px;height:2676px;overflow:hidden}
body{font-family:"Open Sans",Arial,sans-serif;color:var(--ink);background:var(--white);font-size:13px;line-height:1.5}
.wrap{width:900px;margin:0 auto;position:relative}

/* header */
.site-header{height:48px;background:var(--white);border-bottom:1px solid var(--line)}
.site-header .wrap{display:flex;align-items:center;justify-content:space-between;height:48px}
.brand{display:flex;align-items:center;gap:8px;font-weight:700;font-size:22px;color:var(--blue)}
.brand-dot{width:20px;height:20px;border-radius:50%;background:var(--blue)}
.nav{display:flex;gap:4px;list-style:none}
.nav a{display:block;padding:6px 14px;font-size:12px;color:var(--ink);text-decoration:none}
.nav a.active{background:var(--blue);color:var(--white)}

/* hero */
.hero{height:672px;position:relative;background:linear-gradient(100deg,#cfd9e0 0%,#b9c5cd 30%,#8b98a2 55%,#d8dee3 80%,#eef1f3 100%)}
.appointment{position:absolute;left:50%;top:280px;transform:translateX(-50%);width:640px;padding:30px 40px 32px;background:rgba(40,48,56,.55);color:var(--white);text-align:center}
.appointment h2{font-size:26px;font-weight:400;margin-bottom:22px}
.fields{display:grid;grid-template-columns:1fr 1fr;gap:14px 20px;margin-bottom:22px}
.field{height:34px;background:rgba(255,255,255,.92);color:var(--muted);font-size:12px;text-align:left;padding:8px 12px}
.btn{display:inline-block;background:var(--blue);color:var(--white);font-size:12px;padding:8px 30px;border:0}

/* welcome */
.welcome{height:220px;background:var(--blue);color:var(--white);text-align:center;padding-top:38px}
.welcome h1{font-size:26px;font-weight:400;margin-bottom:14px}
.welcome p{font-size:11px;max-width:820px;margin:0 auto 10px;opacity:.92}
.btn-ghost{display:inline-block;margin-top:8px;background:var(--blue-dark);color:var(--white);font-size:10px;padding:5px 16px;border:1px solid rgba(255,255,255,.5)}

/* icons */
.services-icons{height:170px;display:flex;justify-content:center;align-items:center;gap:54px}
.icon-circle{width:78px;height:78px;border-radius:50%;border:2px solid var(--blue);display:flex;align-items:center;justify-content:center}
.icon-circle svg{width:38px;height:38px;fill:none;stroke:var(--blue);stroke-width:2.4;stroke-linecap:round;stroke-linejoin:round}

/* calendar + events */
.agenda{height:310px}
.agenda .wrap{display:flex;gap:40px}
.section-title{font-size:19px;font-weight:600;margin-bottom:6px}
.section-title::after{content:"";display:block;width:44px;height:2px;background:var(--blue);margin-top:4px}
.calendar{width:290px}
.cal-head{background:var(--blue);color:var(--white);display:flex;justify-content:space-between;padding:5px 10px;font-size:12px;margin-top:10px}
.cal-table{width:100%;border-collapse:collapse;font-size:11px;text-align:center}
.cal-table th{background:#f0f3f5;font-weight:600;padding:4px 0;border:1px solid var(--line)}
.cal-table td{padding:5px 0;border:1px solid var(--line);background:#fbf7e8}
.cal-table td.off{color:#bbb;background:#fff}
.cal-table td.today{background:var(--blue);color:var(--white)}
.events{flex:1}
.event{display:flex;gap:18px;padding:14px 0;border-bottom:1px solid var(--line)}
.event-date{width:54px;text-align:center;font-size:10px;color:var(--muted)}
.event-date svg{width:34px;height:34px;fill:none;stroke:var(--blue);stroke-width:2}
.event p{font-size:11px;color:var(--muted)}
.event .btn-small{display:block;width:max-content;margin:6px 0 0 auto;font-size:10px;border:1px solid var(--line);padding:3px 12px;color:var(--ink)}

/* gallery */
.gallery{height:500px;position:relative;background:linear-gradient(90deg,#7f93a3 0%,#a8b7c2 40%,#c5d0d7 70%,#8799a7 100%);padding-top:70px}
.tiles{width:900px;margin:0 auto;display:grid;grid-template-columns:repeat(3,1fr);grid-template-rows:170px 170px;gap:12px;padding:12px;background:rgba(255,255,255,.55)}
.tile{position:relative;overflow:hidden}
.tile-photo{position:absolute;inset:0}
.tile-label{position:absolute;left:0;right:0;bottom:0;padding:6px 12px;background:rgba(2,146,205,.82);color:var(--white);font-size:13px;display:flex;justify-content:space-between}
.t1{background:linear-gradient(135deg,#9fb4c3,#d7e2ea)}
.t2{background:linear-gradient(135deg,#c9d5dd,#7d95a8)}
.t3{background:linear-gradient(135deg,#e3e9ee,#a3b5c2)}
.t4{background:linear-gradient(135deg,#8ea8b9,#cfdbe3)}
.t5{background:linear-gradient(135deg,#bccad4,#eef2f5)}
.t6{background:linear-gradient(135deg,#d2dde4,#92a7b6)}

/* features */
.features{height:280px;padding-top:70px}
.features .wrap{display:grid;grid-template-columns:repeat(3,1fr);gap:40px}
.feature-icon{width:34px;height:34px;background:var(--blue);margin-bottom:10px;display:flex;align-items:center;justify-content:center}
.feature-icon svg{width:20px;height:20px;fill:none;stroke:var(--white);stroke-width:2}
.feature h3{font-size:16px;font-weight:700;margin-bottom:6px}
.feature p{font-size:11px;color:var(--muted);margin-bottom:10px}
.feature .btn-small{font-size:10px;border:1px solid var(--line);padding:3px 12px;display:inline-block}

/* testimonials */
.testimonials{height:220px;padding-top:26px}
.testimonials .wrap{display:grid;grid-template-columns:repeat(3,1fr);gap:14px}
.quote{position:relative;background:var(--blue);color:var(--white);text-align:center;padding:34px 30px 18px;height:170px}
.quote-mark{position:absolute;top:-22px;left:50%;transform:translateX(-50%);width:44px;height:44px;border-radius:50%;background:var(--white);color:var(--ink);font-size:34px;line-height:52px;font-weight:700;box-shadow:0 0 0 3px var(--blue)}
.quote h4{font-size:13px;margin-bottom:6px}
.quote p{font-size:11px;opacity:.92}

/* footer */
.site-footer{height:256px;background:var(--footer);color:var(--footer-text);padding-top:40px;position:relative}
.site-footer .wrap{display:grid;grid-template-columns:repeat(3,1fr);gap:50px}
.site-footer h5{color:var(--white);font-size:14px;font-weight:600;margin-bottom:12px}
.site-footer p,.site-footer li{font-size:11px;list-style:none}
.site-footer li::before{content:"› ";color:var(--blue)}
.copyright{position:absolute;left:0;right:0;bottom:0;height:32px;line-height:32px;text-align:center;font-size:10px;background:#222527}
</style>
</head>
<body>

<header class="site-header">
  <div class="wrap">
    <div class="brand"><span class="brand-dot"></span>Vitoplume</div>
    <ul class="nav">
      <li><a class="active" href="#">Home</a></li>
      <li><a href="#">About us</a></li>
      <li><a href="#">Services</a></li>
      <li><a href="#">Health Screening</a></li>
      <li><a href="#">Providers</a></li>
      <li><a href="#">Contacts</a></li>
    </ul>
  </div>
</header>

<section class="hero" role="img" aria-label="Photo of smiling doctors and business people shaking hands">
  <form class="appointment">
    <h2>Fix An Appointment</h2>
    <div class="fields">
      <div class="field">Name</div>
      <div class="field">Phone</div>
      <div class="field">E-mail</div>
      <div class="field">Date</div>
    </div>
    <span class="btn">Submit</span>
  </form>
</section>

<section class="welcome">
  <h1>Welcome to Vitoplume</h1>
  <p>Vitoplume is an online wellness center that helps individuals and companies take charge of their health. Take a health risk assessment, track your activities, aerobic miles and biometric data, and earn points for every goal you complete.</p>
  <p>We offer free health screenings, help members find affordable medication and low-cost lab work, and connect uninsured people with providers.</p>
  <span class="btn-ghost">Read More</span>
</section>

<section class="services-icons">
  <div class="icon-circle"><svg viewBox="0 0 40 40"><path d="M20 33 7 20a7 7 0 0 1 13-9 7 7 0 0 1 13 9Z"/><path d="M10 20h6l2-4 4 8 2-4h6"/></svg></div>
  <div class="icon-circle"><svg viewBox="0 0 40 40"><path d="M16 6h8M18 6v8l-8 16a3 3 0 0 0 3 4h14a3 3 0 0 0 3-4l-8-16V6"/><path d="M13 26h14"/></svg></div>
  <div class="icon-circle"><svg viewBox="0 0 40 40"><path d="M10 6v10a7 7 0 0 0 14 0V6"/><path d="M17 23v4a7 7 0 0 0 14 0v-3"/><circle cx="31" cy="21" r="3"/></svg></div>
  <div class="icon-circle"><svg viewBox="0 0 40 40"><circle cx="20" cy="13" r="6"/><path d="M8 34a12 12 0 0 1 24 0"/><path d="M20 24v6M17 27h6"/></svg></div>
  <div class="icon-circle"><svg viewBox="0 0 40 40"><rect x="9" y="7" width="22" height="28" rx="2"/><path d="M15 7V4h10v3M14 16h12M14 22h12M14 28h8"/></svg></div>
  <div class="icon-circle"><svg viewBox="0 0 40 40"><rect x="6" y="12" width="28" height="20" rx="2"/><path d="M15 12V8h10v4M20 17v10M15 22h10"/></svg></div>
</section>

<section class="agenda">
  <div class="wrap">
    <div class="calendar">
      <h2 class="section-title">Calendar</h2>
      <div class="cal-head"><span>‹</span><span>July 2017</span><span>›</span></div>
      <table class="cal-table">
        <tr><th>Su</th><th>Mo</th><th>Tu</th><th>We</th><th>Th</th><th>Fr</th><th>Sa</th></tr>
        <tr><td class="off">25</td><td class="off">26</td><td class="off">27</td><td class="off">28</td><td class="off">29</td><td class="off">30</td><td>1</td></tr>
        <tr><td>2</td><td>3</td><td>4</td><td>5</td><td>6</td><td>7</td><td>8</td></tr>
        <tr><td>9</td><td>10</td><td>11</td><td>12</td><td class="today">13</td><td>14</td><td>15</td></tr>
        <tr><td>16</td><td>17</td><td>18</td><td>19</td><td>20</td><td>21</td><td>22</td></tr>
        <tr><td>23</td><td>24</td><td>25</td><td>26</td><td>27</td><td>28</td><td>29</td></tr>
        <tr><td>30</td><td>31</td><td class="off">1</td><td class="off">2</td><td class="off">3</td><td class="off">4</td><td class="off">5</td></tr>
      </table>
    </div>
    <div class="events">
      <h2 class="section-title">Upcoming Events</h2>
      <div class="event">
        <div class="event-date"><svg viewBox="0 0 34 34"><rect x="4" y="7" width="26" height="23" rx="2"/><path d="M4 13h26M11 4v6M23 4v6"/></svg><br>18th Sept</div>
        <div><p>Free community health screening at our partner clinic. Blood pressure, glucose and cholesterol checks for all ages, no insurance needed.</p><span class="btn-small">Read More</span></div>
      </div>
      <div class="event">
        <div class="event-date"><svg viewBox="0 0 34 34"><rect x="4" y="7" width="26" height="23" rx="2"/><path d="M4 13h26M11 4v6M23 4v6"/></svg><br>25th Sept</div>
        <div><p>Wellness workshop on affordable medication and low-cost lab work. Learn how members can lower the cost of their care each year.</p><span class="btn-small">Read More</span></div>
      </div>
    </div>
  </div>
</section>

<section class="gallery" role="img" aria-label="Background photo of a medical team in a hospital corridor">
  <div class="tiles">
    <div class="tile"><div class="tile-photo t1" role="img" aria-label="Photo of doctors in a meeting"></div><div class="tile-label"><span>Health Risk</span><span>›</span></div></div>
    <div class="tile"><div class="tile-photo t2" role="img" aria-label="Photo of a doctor at a desk"></div><div class="tile-label"><span>Free Screening</span><span>›</span></div></div>
    <div class="tile"><div class="tile-photo t3" role="img" aria-label="Photo of a lab technician"></div><div class="tile-label"><span>Free Lab Work</span><span>›</span></div></div>
    <div class="tile"><div class="tile-photo t4" role="img" aria-label="Photo of a patient with a nurse"></div><div class="tile-label"><span>Medication</span><span>›</span></div></div>
    <div class="tile"><div class="tile-photo t5" role="img" aria-label="Photo of test tubes in a laboratory"></div><div class="tile-label"><span>Lab Assist</span><span>›</span></div></div>
    <div class="tile"><div class="tile-photo t6" role="img" aria-label="Photo of a doctor with a tablet"></div><div class="tile-label"><span>Free Clinics</span><span>›</span></div></div>
  </div>
</section>

<section class="features">
  <div class="wrap">
    <div class="feature">
      <div class="feature-icon"><svg viewBox="0 0 20 20"><path d="M10 17 3 10a4 4 0 0 1 7-5 4 4 0 0 1 7 5Z"/></svg></div>
      <h3>Lorem Ipsum is simply</h3>
      <p>Record health activities, aerobic miles and biometric data, and watch your progress toward your goals.</p>
      <span class="btn-small">Read More</span>
    </div>
    <div class="feature">
      <div class="feature-icon"><svg viewBox="0 0 20 20"><rect x="3" y="4" width="14" height="13"/><path d="M3 8h14M7 2v4M13 2v4"/></svg></div>
      <h3>Lorem Ipsum is simply</h3>
      <p>Book a free yearly physical with a provider if you are uninsured and cannot pay out of pocket.</p>
      <span class="btn-small">Read More</span>
    </div>
    <div class="feature">
      <div class="feature-icon"><svg viewBox="0 0 20 20"><path d="M4 10l4 4 8-8"/></svg></div>
      <h3>Lorem Ipsum is simply</h3>
      <p>Earn points for every completed activity and redeem them for rewards across our wellness portal.</p>
      <span class="btn-small">Read More</span>
    </div>
  </div>
</section>

<section class="testimonials">
  <div class="wrap">
    <div class="quote"><span class="quote-mark">“</span><h4>John</h4><p>Vitoplume helped me find affordable medication and a free check-up. I feel healthier than ever.</p></div>
    <div class="quote"><span class="quote-mark">“</span><h4>John</h4><p>The activity tracker keeps me motivated, and the points make every workout worth it.</p></div>
    <div class="quote"><span class="quote-mark">“</span><h4>John</h4><p>Low-cost lab work through Vitoplume saved my family money this year.</p></div>
  </div>
</section>

<footer class="site-footer">
  <div class="wrap">
    <div>
      <h5>About us</h5>
      <p>Vitoplume is an online wellness center in Chicago, IL. We help individuals and companies assess health risks and lower the cost of care.</p>
      <p style="margin-top:8px;color:var(--white)">» Read More</p>
    </div>
    <div>
      <h5>Services</h5>
      <ul>
        <li>Health risk assessments</li>
        <li>Free health screenings</li>
        <li>Affordable medications</li>
        <li>Low-cost lab work</li>
        <li>Free clinic providers</li>
      </ul>
    </div>
    <div>
      <h5>Get in Touch</h5>
      <p>+1 (312) 555-0148</p>
      <p>hello@vitoplume.com</p>
      <p>www.vitoplume.com</p>
      <p>Chicago, IL</p>
    </div>
  </div>
  <div class="copyright">Copyright © 2017 Vitoplume. All rights reserved.</div>
</footer>

</body>
</html>
```